Van wrap design for 2014 Marlow T310 Commercial Van

We are launching a maintenance division for our property company and have bought a new van to advertise our maintenance company. We will be advertising to property owners, the general public etc. our services.
We wish the text to read: Maintenance Division - remodels, plumbing & electrical.

Requirements
Must have
• Both images attached

```html
<!DOCTYPE html>
<html lang="en">
<head>
<meta charset="utf-8">
<title>Harlow Brothers Properties – Maintenance Division Van Wrap</title>
<link href="https://fonts.googleapis.com/css2?family=Oswald:wght@500;600&family=Roboto+Condensed:wght@500&family=Roboto:wght@500&display=swap" rel="stylesheet">
<style>
  :root {
    --page: #ffffff;
    --wrap-white: #ffffff;
    --wrap-black: #141414;
    --wrap-grey: #8a8a8a;
    --text-dark: #111111;
    --text-grey: #8c8c8c;
    --text-light: #ffffff;
    --photo-top: #e9eaec;
    --photo-bottom: #9a9da3;
  }
  * { margin: 0; padding: 0; box-sizing: border-box; }
  html, body {
    width: 1200px; height: 686px; overflow: hidden;
    background: var(--page);
  }
  .canvas { position: relative; width: 1200px; height: 686px; }
  .wrap-panel {
    position: absolute; left: 40px; top: 171px;
    width: 1120px; height: 344px;
    background: var(--wrap-white);
    box-shadow: 0 0 0 1px #e4e4e4;
    overflow: hidden;
  }
  .wrap-shapes { position: absolute; inset: 0; }
  .team-photo {
    position: absolute; inset: 0;
    background: linear-gradient(180deg, var(--photo-top) 0%, #c9cbcf 55%, var(--photo-bottom) 100%);
    clip-path: polygon(690px 0, 1060px 0, 1000px 344px, 752px 344px);
  }
  .services {
    position: absolute; left: 228px; top: 118px;
    font-family: "Oswald", sans-serif; font-weight: 500;
    color: var(--text-dark); text-transform: uppercase;
  }
  .services__title { font-size: 21px; line-height: 24px; letter-spacing: 0.3px; }
  .services__subtitle {
    font-size: 19px; line-height: 22px; color: var(--text-grey);
    padding-bottom: 5px; border-bottom: 2px solid var(--text-dark);
    width: 112px; margin-bottom: 12px;
  }
  .services__list { list-style: none; }
  .services__item {
    display: flex; align-items: center; gap: 8px;
    font-size: 20px; line-height: 31px;
  }
  .services__item--grey { color: var(--text-grey); }
  .services__icon { width: 14px; height: 14px; flex: none; }
  .brand {
    position: absolute; left: 475px; top: 56px; width: 170px;
    font-family: "Oswald", sans-serif; font-weight: 500;
    color: var(--text-light); text-transform: uppercase;
    font-size: 22px; line-height: 24px; letter-spacing: 1px; text-align: center;
  }
  .brand__square {
    display: block; width: 34px; height: 34px; margin: 0 auto 10px;
    border: 3px solid var(--text-light);
  }
  .contact {
    position: absolute; left: 430px; top: 200px; width: 260px;
    text-align: center; color: var(--text-light);
  }
  .contact__phone {
    font-family: "Roboto Condensed", sans-serif; font-weight: 500;
    font-size: 44px; line-height: 50px; letter-spacing: 0.5px;
  }
  .contact__web {
    font-family: "Roboto", sans-serif; font-weight: 500;
    font-size: 25px; line-height: 32px; letter-spacing: 0.5px;
  }
</style>
</head>
<body>
<div class="canvas">
  <div class="wrap-panel">
    <svg class="wrap-shapes" viewBox="0 0 1120 344" width="1120" height="344" aria-hidden="true">
      <polygon class="band-black" points="390,0 690,0 752,344 450,344" fill="var(--wrap-black)"/>
      <polygon class="stripe-grey" points="360,120 378,120 414,344 396,344" fill="var(--wrap-grey)"/>
    </svg>
    <div class="team-photo" role="img" aria-label="Photo of the two brothers who run the company, in suits, smiling"></div>
    <svg class="wrap-shapes" viewBox="0 0 1120 344" width="1120" height="344" aria-hidden="true">
      <polygon class="stripe-grey" points="688,0 704,0 766,344 750,344" fill="var(--wrap-grey)"/>
      <polygon class="accent-grey" points="1010,110 1040,80 1030,300 960,320" fill="var(--wrap-grey)"/>
      <polygon class="end-white" points="1044,0 1060,0 1000,344 984,344" fill="var(--wrap-white)"/>
      <polygon class="end-black" points="1060,0 1120,0 1120,344 1000,344" fill="var(--wrap-black)"/>
    </svg>

    <div class="services">
      <p class="services__title">Maintenance</p>
      <p class="services__subtitle">Division</p>
      <ul class="services__list">
        <li class="services__item"><svg class="services__icon" viewBox="0 0 14 14"><path d="M3 2 L10 7 L3 12" fill="none" stroke="currentColor" stroke-width="2"/></svg>Remodels</li>
        <li class="services__item services__item--grey"><svg class="services__icon" viewBox="0 0 14 14"><path d="M3 2 L10 7 L3 12" fill="none" stroke="currentColor" stroke-width="2"/></svg>Plumbing</li>
        <li class="services__item"><svg class="services__icon" viewBox="0 0 14 14"><path d="M3 2 L10 7 L3 12" fill="none" stroke="currentColor" stroke-width="2"/></svg>Electrical.</li>
      </ul>
    </div>

    <div class="brand">
      <span class="brand__square"></span>
      Harlow<br>Brothers<br>Properties
    </div>

    <div class="contact">
      <p class="contact__phone">0198 765 432</p>
      <p class="contact__web">www.hbph.net</p>
    </div>
  </div>
</div>
</body>
</html>
```